Ad to be used on social media.

____________________________________________________________________________

Bored at Home?

Study to become a
Virtual Mortgage Originator today...

Complete 20 Hour Online Course & State Exam
in 30 days or less

Earn $3,000 to $5,000 on average per loan
No Work Hours, Goals or Quotas
Full Time or Part Time Opportunities

Email us at employment@brightlanehomeloans.com

Brightlane Lending Group, Inc.
7200 Marrowdale Lane
Ellicott City, MD 21043
(800) 417-9062
www.brightlanehomeloans.com
NMLS #837160

```html
<!DOCTYPE html>
<html lang="en">
<head>
<meta charset="utf-8">
<title>Bored at Home? – Virtual Mortgage Originator Ad</title>
<link rel="stylesheet" href="https://fonts.googleapis.com/css2?family=Poppins:wght@700;800&family=Open+Sans:wght@400;600&display=swap">
<style>
  :root {
    --brand-red: #e8222a;
    --board: #232323;
    --paper: #ffffff;
    --ink: #333333;
    --photo-light: #eef0f1;
    --photo-mid: #d9dcdf;
    --photo-accent: #35a9d6;
  }
  * { box-sizing: border-box; margin: 0; padding: 0; }
  html, body { width: 1200px; height: 1005px; overflow: hidden; background: var(--board); }
  body { position: relative; font-family: "Open Sans", Arial, sans-serif; color: var(--ink); }

  .ad { position: absolute; background: var(--paper); overflow: hidden; }
  .ad--wide { left: 106px; top: 57px; width: 585px; height: 830px; }
  .ad--narrow { left: 765px; top: 67px; width: 321px; height: 820px; }

  .ad__title, .ad__mark {
    position: absolute; font-family: "Poppins", Arial, sans-serif; font-weight: 700;
    color: var(--brand-red); line-height: 1; white-space: nowrap;
  }
  .ad--wide .ad__title { left: 68px; top: 52px; font-size: 60px; letter-spacing: -0.5px; }
  .ad--wide .ad__mark { left: 508px; top: 18px; font-size: 132px; font-weight: 800; }
  .ad--narrow .ad__title { left: 36px; top: 48px; font-size: 51px; line-height: 55px; letter-spacing: -0.5px; }
  .ad--narrow .ad__mark { left: 258px; top: 76px; font-size: 88px; font-weight: 800; }

  .ad__visual { position: absolute; left: 0; top: 0; }

  .ad__heading {
    position: absolute; font-family: "Poppins", Arial, sans-serif; font-weight: 700;
    color: var(--brand-red); text-transform: uppercase; letter-spacing: -0.2px;
  }
  .ad--wide .ad__heading { left: 27px; top: 526px; font-size: 15.5px; line-height: 22px; }
  .ad--narrow .ad__heading { left: 13px; top: 406px; font-size: 15.5px; line-height: 21.5px; }

  .ad__body { position: absolute; }
  .ad--wide .ad__body { left: 28px; top: 578px; width: 420px; font-size: 17px; line-height: 23px; }
  .ad--narrow .ad__body { left: 17px; top: 476px; width: 292px; font-size: 18px; line-height: 25px; }
  .ad__perks { list-style: none; }
  .ad__perks li { position: relative; padding-left: 20px; }
  .ad__perks li::before { content: "•"; position: absolute; left: 1px; font-size: 0.8em; }
  .ad__highlight { color: var(--brand-red); }

  .ad__email { position: absolute; color: var(--brand-red); font-size: 12px; }
  .ad--wide .ad__email { left: 29px; top: 719px; }
  .ad--narrow .ad__email { left: 21px; top: 702px; font-size: 11.5px; }

  .ad__footer { position: absolute; left: 0; right: 0; bottom: 0; background: var(--brand-red); color: var(--paper); }
  .ad--wide .ad__footer { top: 747px; }
  .ad--narrow .ad__footer { top: 729px; }
  .ad__contact { position: absolute; }
  .ad--wide .ad__contact { left: 30px; top: 7px; font-size: 15.5px; line-height: 21px; }
  .ad--narrow .ad__contact { left: 21px; top: 6px; font-size: 13.5px; line-height: 18px; }
  .ad__company { font-weight: 600; font-size: 0.92em; }
  .ad__web { position: absolute; font-weight: 600; }
  .ad--wide .ad__web { right: 19px; top: 45px; font-size: 13.5px; }
  .ad--narrow .ad__web { right: 5px; top: 71px; font-size: 12.5px; }
</style>
</head>
<body>

<article class="ad ad--wide">
  <svg class="ad__visual" width="585" height="830" viewBox="0 0 585 830">
    <defs>
      <linearGradient id="photoWide" x1="0" y1="0" x2="1" y2="1">
        <stop offset="0" stop-color="#f4f5f6"/>
        <stop offset="0.5" stop-color="#dfe2e4"/>
        <stop offset="0.75" stop-color="#9fc9da"/>
        <stop offset="1" stop-color="#e9e2d6"/>
      </linearGradient>
    </defs>
    <polygon points="0,129 585,207 585,518 0,518" fill="url(#photoWide)" role="img" aria-label="Photo of a young woman studying at a laptop with an orange juice on the table"/>
    <polygon points="0,129 585,183 585,207" fill="var(--brand-red)"/>
  </svg>
  <h1 class="ad__title">Bored at Home</h1>
  <span class="ad__mark" aria-hidden="true">?</span>
  <h2 class="ad__heading">Study to become a<br>Virtual Mortgage Originator today...</h2>
  <div class="ad__body">
    <p>Complete 20 Hour Online Course &amp; State Exam in 30 days or less</p>
    <ul class="ad__perks">
      <li><span class="ad__highlight">Earn $3,000 to $5,000</span> on average per loan</li>
      <li>No Work Hours, Goals or Quotas</li>
      <li>Full Time or Part Time Opportunities</li>
    </ul>
  </div>
  <p class="ad__email">Email us at employment@brightlanehomeloans.com</p>
  <footer class="ad__footer">
    <address class="ad__contact" style="font-style:normal">
      <div class="ad__company">Brightlane Lending Group, Inc.</div>
      <div>7200 Marrowdale Lane, Ellicott City, MD 21043</div>
      <div>(800) 417-9062</div>
    </address>
    <div class="ad__web">www.brightlanehomeloans.com</div>
  </footer>
</article>

<article class="ad ad--narrow">
  <svg class="ad__visual" width="321" height="820" viewBox="0 0 321 820">
    <defs>
      <linearGradient id="photoNarrow" x1="0" y1="0" x2="1" y2="1">
        <stop offset="0" stop-color="#f4f5f6"/>
        <stop offset="0.5" stop-color="#dfe2e4"/>
        <stop offset="0.75" stop-color="#9fc9da"/>
        <stop offset="1" stop-color="#e9e2d6"/>
      </linearGradient>
    </defs>
    <polygon points="0,171 321,214 321,383 0,383" fill="url(#photoNarrow)" role="img" aria-label="Photo of a young woman studying at a laptop with an orange juice on the table"/>
    <polygon points="0,171 321,199 321,214" fill="var(--brand-red)"/>
  </svg>
  <h1 class="ad__title">Bored<br>at Home</h1>
  <span class="ad__mark" aria-hidden="true">?</span>
  <h2 class="ad__heading">Study to become a<br>Virtual Mortgage Originator<br>today...</h2>
  <div class="ad__body">
    <p>Complete 20 Hour Online Course &amp; State Exam in 30 days or less</p>
    <ul class="ad__perks">
      <li><span class="ad__highlight">Earn $3,000 to $5,000</span> on average per loan</li>
      <li>No Work Hours, Goals or Quotas</li>
      <li>Full Time or Part Time Opportunities</li>
    </ul>
  </div>
  <p class="ad__email">Email us at employment@brightlanehomeloans.com</p>
  <footer class="ad__footer">
    <address class="ad__contact" style="font-style:normal">
      <div class="ad__company">Brightlane Lending Group, Inc.</div>
      <div>7200 Marrowdale Lane, Ellicott City, MD 21043</div>
      <div>(800) 417-9062</div>
    </address>
    <div class="ad__web">www.brightlanehomeloans.com</div>
  </footer>
</article>

</body>
</html>
```